Brindlecove Partners needs a business card design

We need a new business card design using the logo recently selected in a logo competition on Pixel Arena. Our business is a consultancy specializing in aviation and energy and the winning business card design will promote an image of precision and professionalism with creativity.

Please use the logo with the name on the front of the card and use a complementary font. Make the back white with either the light grey or dark grey logo.

Target Market(s)

Senior finance and legal leaders at aviation and energy companies

Industry/Entity Type

Management Consulting

Contact Information for Business Card

Peter Dunstable
President
Brindlecove Partners

www.brindlecovepartners.example

(713) 555-0147
pd@brindlecovepartners.example

Requirements
Must have
• Professional font that goes well with the logo font

```html
<!DOCTYPE html>
<html lang="en">
<head>
<meta charset="utf-8">
<title>Brindlecove Partners — Business Card</title>
<link rel="stylesheet" href="https://fonts.googleapis.com/css2?family=PT+Sans:wght@400;700&display=swap">
<style>
  :root {
    --sky-deep: #3a84c0;
    --sky-mid: #4b98d2;
    --sky-light: #9cc6e6;
    --mist: #e3e5e7;
    --brand-navy: #1f2f8f;
    --name-blue: #1530d8;
    --title-red: #8a1010;
    --contact-white: #eef4fa;
  }
  * { margin: 0; padding: 0; box-sizing: border-box; }
  html, body {
    width: 1200px; height: 686px; overflow: hidden;
    background: #ffffff;
  }
  .card {
    position: relative;
    width: 1200px; height: 686px;
    overflow: hidden;
    font-family: "PT Sans", Arial, sans-serif;
  }
  .card__backdrop {
    position: absolute; inset: 0;
    background:
      radial-gradient(ellipse 560px 430px at 130px 150px, var(--mist) 0%, var(--mist) 38%, rgba(227,229,231,0.85) 52%, rgba(156,198,230,0) 100%),
      radial-gradient(ellipse 900px 620px at 260px 260px, var(--sky-light) 0%, var(--sky-mid) 55%, rgba(75,152,210,0) 100%),
      linear-gradient(160deg, var(--sky-mid) 0%, var(--sky-deep) 60%, #3a80bc 100%);
  }
  .brand {
    position: absolute;
    left: 58px; top: 176px;
    color: var(--brand-navy);
    font-size: 34px;
    font-weight: 400;
    letter-spacing: 4px;
    line-height: 42px;
    text-transform: uppercase;
  }
  .identity {
    position: absolute;
    right: 44px; top: 388px;
    text-align: right;
    font-variant: small-caps;
  }
  .identity__name {
    display: inline-block;
    color: var(--name-blue);
    font-size: 44px;
    font-weight: 400;
    letter-spacing: 7px;
    line-height: 44px;
    border-bottom: 1.5px solid var(--name-blue);
    padding: 0 0 2px 2px;
  }
  .identity__title {
    margin-top: 18px;
    color: var(--title-red);
    font-size: 25px;
    font-weight: 400;
    letter-spacing: 1.5px;
    line-height: 29px;
    padding-right: 4px;
  }
  .contacts {
    position: absolute;
    left: 564px; top: 532px;
    list-style: none;
  }
  .contacts__item {
    display: flex; align-items: center;
    height: 43px;
    color: var(--contact-white);
    font-size: 25px;
  }
  .contacts__icon {
    width: 32px; height: 32px;
    margin-right: 22px;
    flex: none;
  }
</style>
</head>
<body>
  <main class="card">
    <div class="card__backdrop" role="img" aria-label="Soft blue and pale grey background with sweeping light curves"></div>

    <div class="brand">Brindlecove<br>Partners</div>

    <section class="identity">
      <h1 class="identity__name">Peter Dunstable</h1>
      <p class="identity__title">President<br>Brindlecove Partners</p>
    </section>

    <ul class="contacts">
      <li class="contacts__item">
        <svg class="contacts__icon" viewBox="0 0 32 32" aria-hidden="true">
          <rect x="9" y="3" width="14" height="26" rx="2.5" fill="none" stroke="var(--contact-white)" stroke-width="2.2"/>
          <line x1="13" y1="7" x2="19" y2="7" stroke="var(--contact-white)" stroke-width="1.6"/>
          <circle cx="16" cy="25" r="1.4" fill="var(--contact-white)"/>
        </svg>
        <span>(713) 555-0147</span>
      </li>
      <li class="contacts__item">
        <svg class="contacts__icon" viewBox="0 0 32 32" aria-hidden="true">
          <rect x="3" y="8" width="26" height="17" fill="none" stroke="var(--contact-white)" stroke-width="2"/>
          <path d="M3 8 L16 19 L29 8" fill="none" stroke="var(--contact-white)" stroke-width="2"/>
        </svg>
        <span>pd@brindlecovepartners.example</span>
      </li>
      <li class="contacts__item">
        <svg class="contacts__icon" viewBox="0 0 32 32" aria-hidden="true">
          <rect x="3" y="6" width="26" height="21" rx="1.5" fill="none" stroke="var(--contact-white)" stroke-width="2"/>
          <line x1="3" y1="11" x2="29" y2="11" stroke="var(--contact-white)" stroke-width="2"/>
          <line x1="8" y1="19" x2="24" y2="19" stroke="var(--contact-white)" stroke-width="2"/>
        </svg>
        <span>www.brindlecovepartners.example</span>
      </li>
    </ul>
  </main>
</body>
</html>
```